Help us make a CLOVERTON impact! Saving Dogs from Kill Shelters.....

*Our mission is to save Dogs from kill shelters, and unite them with responsible families nationwide.

*We would love to incorporate sacred geometry into our message. The "Flower of Life" needs to be incorporated into this design.Earth Friendly Self-Sustainable Animal Shelter is a goal. Solar Power

*We want the professional look of exclusiveness.

*The logo/brand is not set in stone, and we welcome opinions!

***Earth Consciousness. Awareness. Love.

Peace. LOVE. Adopt. :)

I would like a sleek exclusive look, one that says WOW. This design needs to have a good energy about it. I have envisioned the front being logo only and vertical. Please have a look at our Linkspace page to get a feel about what we are doing & trying to accomplish...

*ONE Side Card
**The flower of life inlay needs to be in or around of the logo.
***The following is the ONLY information I want on the card!

CLOVERTON Adoption Center

Maren Hollis

www.CLOVERTONadoptioncenter.com

(555)013-4478

FB Icon

Target Market(s)

Stable, Wealthy, Responsible Families in the Northeast.

Industry/Entity Type

Solar

Contact Information for Business Card

CLOVERTON Adoption Center, Maren Hollis, Founder/Director, 912 Birchwood Court, Bath Springs, TN 40927, (555)013-4478, FB Icon

Requirements
Must have
• FB icon on back.
The "Flower of Life" must be incorporated into this design.
Nice to have
• Positive Energy
Bright Colors
WOW Factor

```html
<!DOCTYPE html>
<html lang="en">
<head>
<meta charset="utf-8">
<title>CLOVERTON Adoption Center – Business Card</title>
<link rel="stylesheet" href="https://fonts.googleapis.com/css2?family=Oswald:wght@600;700&family=Arimo:wght@400;700&display=swap">
<style>
  :root {
    --page-bg: #e6e6e6;
    --card-white: #ffffff;
    --leaf-green: #1f9a3c;
    --deep-green: #0f7a2c;
    --lime: #c9dc1e;
    --lime-bright: #e4ef3a;
    --text-light: #ffffff;
    --brand-green: #23963a;
  }
  * { margin: 0; padding: 0; box-sizing: border-box; }
  html, body {
    width: 1200px; height: 900px; overflow: hidden;
    background: var(--page-bg);
  }
  .canvas { position: relative; width: 1200px; height: 900px; }
  .business-card {
    position: absolute; left: 120px; top: 170px;
    width: 960px; height: 560px;
    border-radius: 44px; overflow: hidden;
    background: var(--card-white);
    box-shadow: 0 18px 40px rgba(0,0,0,0.18);
  }
  .card-background { position: absolute; inset: 0; width: 100%; height: 100%; }
  .brand-mark {
    position: absolute; left: 40px; top: 240px; width: 360px;
    display: flex; align-items: center; justify-content: center; gap: 14px;
    font-family: "Oswald", sans-serif; font-weight: 700; font-size: 54px;
    color: var(--brand-green); line-height: 1;
  }
  .brand-mark .mark-dot {
    width: 38px; height: 38px; border-radius: 50%;
    background: var(--lime);
  }
  .card-info { position: absolute; inset: 0; color: var(--text-light); font-family: "Arimo", sans-serif; }
  .org-name {
    position: absolute; left: 520px; width: 380px; top: 70px; text-align: center;
    font-family: "Oswald", sans-serif; font-weight: 700; font-size: 74px; line-height: 1;
    color: var(--lime-bright); letter-spacing: 1px;
  }
  .org-tagline {
    position: absolute; left: 520px; width: 380px; top: 158px; text-align: center;
    font-size: 30px;
  }
  .contact-name {
    position: absolute; left: 560px; top: 250px;
    font-size: 28px; font-weight: 700; color: var(--lime-bright);
  }
  .contact-phone {
    position: absolute; left: 520px; width: 380px; top: 322px; text-align: center;
    font-size: 29px;
  }
  .contact-web {
    position: absolute; right: 40px; top: 372px; text-align: right;
    font-size: 25px; font-weight: 700;
  }
  .social-link {
    position: absolute; right: 40px; top: 448px;
    display: flex; align-items: center; gap: 10px;
    font-size: 26px; font-weight: 700;
  }
  .social-link .social-square {
    width: 32px; height: 32px; border-radius: 6px; background: var(--text-light);
  }
</style>
</head>
<body>
<main class="canvas">
  <section class="business-card" aria-label="CLOVERTON Adoption Center business card">
    <svg class="card-background" viewBox="0 0 960 560" preserveAspectRatio="none" aria-hidden="true">
      <defs>
        <linearGradient id="greenFill" x1="0" y1="0" x2="0" y2="1">
          <stop offset="0" stop-color="#22a64a"/>
          <stop offset="1" stop-color="#0c6f28"/>
        </linearGradient>
        <linearGradient id="limeFill" x1="0" y1="0" x2="0" y2="1">
          <stop offset="0" stop-color="#e4ef3a"/>
          <stop offset="1" stop-color="#9cc41c"/>
        </linearGradient>
      </defs>
      <path d="M505 0 H960 V560 H355 C330 360 400 160 505 0 Z" fill="url(#limeFill)"/>
      <path d="M540 0 H960 V560 H380 C360 360 430 160 540 0 Z" fill="url(#greenFill)"/>
      <path d="M0 0 H505 C400 160 330 360 355 560 H0 Z" fill="#ffffff"/>
    </svg>

    <div class="brand-mark" role="img" aria-label="Organisation logo: CLOVERTON">
      <span class="mark-dot"></span>
      <span class="mark-name">CLOVERTON</span>
    </div>

    <div class="card-info">
      <h1 class="org-name">CLOVERTON</h1>
      <p class="org-tagline">Adoption Center</p>
      <p class="contact-name">Maren Hollis</p>
      <p class="contact-phone">(555)013-4478</p>
      <p class="contact-web">www.CLOVERTONadoptioncenter.com</p>
      <p class="social-link">Like us on Linkspace <span class="social-square"></span></p>
    </div>
  </section>
</main>
</body>
</html>
```